Accounting Practice Business Card Design

I have a logo I am happy for you to use in the design of the Business Card.
You can edit and change colours as you please, I am not fixated on it.
I am looking for a modern and clean overall feel for the finished design.

The business is a small accounting practice who thrives on word of mouth referrals and this card will be given to all current and prospect clients.

Industry/Entity Type

Accountant

Contact Information for Business Card

Marcus Elwin
Level 5, 8 Corvale Ridge Road
ASHGROVE RISE VIC 3187
Phone: 9481 3057
Email: melwin@mrfaccountants.com.au
Web: www.mrfaccountants.com.au

Font styles to use
Serif
Sans Serif

Colors
0555a3
3277b5
85acd3
0393ce
33a6d7
85cae6
00a990
33b8a4
9bcb3c

Requirements
Must have
• "Your tax worries end the day you call us in"
• "Every word of mouth referral means the world"
Nice to have
• Modern clean professional

```html
<!DOCTYPE html>
<html lang="en">
<head>
<meta charset="utf-8">
<title>MRF Accountants – Business Card</title>
<link href="https://fonts.googleapis.com/css2?family=Roboto:ital,wght@0,400;0,700;0,900;1,500&family=Roboto+Condensed:wght@700&display=swap" rel="stylesheet">
<style>
  :root {
    --backdrop: #e9e6e1;
    --paper: #f7f7f6;
    --navy: #0e4779;
    --forest: #2f6b34;
    --white: #ffffff;
    --shadow: 0 3px 8px rgba(0,0,0,0.35);
  }
  * { margin: 0; padding: 0; box-sizing: border-box; }
  html, body {
    width: 1200px; height: 960px; overflow: hidden;
    background: var(--backdrop);
    font-family: "Roboto", Arial, sans-serif;
  }
  .stage { position: relative; width: 1200px; height: 960px; }

  .card {
    position: absolute; width: 600px; height: 343px;
    box-shadow: var(--shadow); overflow: hidden;
  }
  .card--front { left: 314px; top: 113px; background: var(--paper); }
  .card--back { left: 311px; top: 472px; background: var(--forest); }

  .band { position: absolute; left: 0; width: 100%; }
  .card--front .band--navy { top: 167px; height: 148px; background: var(--navy); }
  .card--front .band--forest { top: 315px; height: 28px; background: var(--forest); }
  .card--back .band--navy { top: 269px; height: 51px; background: var(--navy); }

  .wordmark {
    position: absolute; font-weight: 900; line-height: 0.9;
    text-align: left; letter-spacing: -0.5px;
  }
  .wordmark__main { display: block; }
  .wordmark__sub { display: block; letter-spacing: 0.3px; }
  .card--front .wordmark { left: 327px; top: 42px; color: var(--navy); }
  .card--front .wordmark__main { font-size: 86px; }
  .card--front .wordmark__sub { font-size: 25px; margin-top: -6px; }
  .card--back .wordmark { left: 167px; top: 98px; color: var(--white); }
  .card--back .wordmark__main { font-size: 122px; }
  .card--back .wordmark__sub { font-size: 35px; margin-top: -12px; }

  .holder-name {
    position: absolute; left: 45px; top: 229px;
    font-family: "Roboto Condensed", "Arial Narrow", sans-serif;
    font-weight: 700; font-size: 20px; color: var(--white);
  }

  .contact {
    position: absolute; left: 327px; top: 189px;
    color: var(--white); font-size: 14px; line-height: 18px;
  }
  .contact__address { margin-bottom: 10px; }
  .contact__row { display: flex; align-items: center; gap: 8px; height: 19px; }
  .contact__icon { width: 13px; height: 13px; flex: none; }

  .tagline {
    position: absolute; left: 0; top: 276px; width: 100%;
    text-align: center; color: var(--white);
    font-style: italic; font-weight: 500; font-size: 14px; line-height: 18px;
  }
</style>
</head>
<body>
<main class="stage">
  <section class="card card--front" aria-label="Card front">
    <div class="wordmark">
      <span class="wordmark__main">MRF</span>
      <span class="wordmark__sub">ACCOUNTANTS</span>
    </div>
    <div class="band band--navy"></div>
    <div class="band band--forest"></div>
    <p class="holder-name">MARCUS ELWIN</p>
    <div class="contact">
      <p class="contact__address">Level 5, 8 Corvale Ridge Road<br>ASHGROVE RISE VIC 3187</p>
      <p class="contact__row">
        <svg class="contact__icon" viewBox="0 0 16 16" aria-hidden="true"><path fill="#fff" d="M3.6 1.2l2.2 2.6c.3.4.3.9 0 1.3L4.7 6.4c.9 2 2.6 3.8 4.8 4.8l1.3-1.1c.4-.3.9-.3 1.3 0l2.6 2.2c.4.3.4.9.1 1.3l-1.3 1.3C11.8 16.6 0 8 1 2.5l1.3-1.3c.4-.3 1-.3 1.3 0z"/></svg>
        <span>9481 3057</span>
      </p>
      <p class="contact__row">
        <svg class="contact__icon" viewBox="0 0 16 16" aria-hidden="true"><rect x="1" y="3" width="14" height="10" fill="#fff"/><path d="M1.5 3.5L8 9l6.5-5.5" fill="none" stroke="#0e4779" stroke-width="1.4"/></svg>
        <span>melwin@mrfaccountants.com.au</span>
      </p>
      <p class="contact__row">
        <svg class="contact__icon" viewBox="0 0 16 16" aria-hidden="true"><circle cx="8" cy="8" r="7" fill="#fff"/><path d="M1 8h14M8 1c-3 3.5-3 10.5 0 14M8 1c3 3.5 3 10.5 0 14" fill="none" stroke="#0e4779" stroke-width="1"/></svg>
        <span>www.mrfaccountants.com.au</span>
      </p>
    </div>
  </section>

  <section class="card card--back" aria-label="Card back">
    <div class="wordmark">
      <span class="wordmark__main">MRF</span>
      <span class="wordmark__sub">ACCOUNTANTS</span>
    </div>
    <div class="band band--navy"></div>
    <p class="tagline">Your tax worries end the day you call us in<br>Every word of mouth referral means the world</p>
  </section>
</main>
</body>
</html>
```